Harbourline capital partners pty ltd

Hi guys I recently opened a brokerage company. I need a flyer to capture the attention of customers.
I would like something professional and cool at the same time.
My website is harbourcp-example.com.au
I also attached the current flyer. as you can see it lacks of originality and it isn't cool!!!!
Thank you

Target Market(s)

People between the age of 18-50

Industry/Entity Type

Financial Service

Requirements
Must have
• Mast have features and contents that reflects the website
• harbourcp-example.com.au
Nice to have
• Open to anything
Should not have
• Not to sure

```html
<!DOCTYPE html>
<html lang="en">
<head>
<meta charset="utf-8">
<title>Harbourline Capital Partners – Flyer</title>
<link href="https://fonts.googleapis.com/css2?family=Didact+Gothic&family=Montserrat:wght@600;700&display=swap" rel="stylesheet">
<style>
  :root {
    --page-bg: #d9d9db;
    --paper: #ffffff;
    --brand-blue: #1c9ad6;
    --brand-orange: #f7941d;
    --orange-soft: #fbc27a;
    --orange-pale: #fde3c2;
    --ink: #231f20;
    --ink-soft: #3d3a3b;
    --hero-grey: #e5e5e7;
    --badge-yellow: #fde08a;
    --badge-green: #7fcfae;
    --badge-salmon: #f4876f;
  }
  * { box-sizing: border-box; margin: 0; padding: 0; }
  html, body { width: 1061px; height: 1200px; overflow: hidden; }
  body { background: var(--page-bg); font-family: "Didact Gothic", sans-serif; color: var(--ink); }

  .flyer {
    position: absolute; left: 114px; top: 14px;
    width: 832px; height: 1172px;
    background: var(--paper);
    box-shadow: 0 4px 18px rgba(0,0,0,.25);
    overflow: hidden;
  }

  .brand { position: absolute; left: 42px; top: 70px; display: flex; align-items: center; gap: 12px; }
  .brand__mark { width: 18px; height: 18px; background: var(--brand-blue); }
  .brand__name {
    font-family: "Didact Gothic", sans-serif; color: var(--brand-blue);
    font-size: 22px; line-height: 1.15; text-transform: uppercase; letter-spacing: .5px;
  }

  .contact-top { position: absolute; right: 36px; top: 70px; text-align: right; }
  .contact-top__web { font-size: 19px; color: var(--ink); }
  .contact-top__phone { font-family: "Montserrat", sans-serif; font-weight: 700; font-size: 31px; margin-top: 6px; color: var(--ink); }

  .hero { position: absolute; left: 0; top: 147px; width: 832px; height: 448px; background: var(--hero-grey); overflow: hidden; }
  .hero__glow { position: absolute; left: 20px; top: 30px; width: 380px; height: 380px; border-radius: 50%; background: #f3f3f4; }
  .hero__portrait {
    position: absolute; left: 70px; top: 28px; width: 266px; height: 420px;
    background: linear-gradient(180deg, #cfc7c2 0%, #8b6a58 45%, #6e5142 100%);
    border-radius: 120px 120px 0 0;
  }
  .hero__rule { position: absolute; left: 0; bottom: 0; width: 100%; height: 4px; background: #d3d3d6; }

  .services { position: absolute; left: 0; top: 0; width: 832px; height: 448px; }
  .services__title { position: absolute; left: 428px; top: 180px; width: 228px; text-align: center; color: var(--ink); }
  .services__lead { font-size: 25px; }
  .services__main { font-family: "Montserrat", sans-serif; font-weight: 700; font-size: 40px; color: #fff; letter-spacing: 1px; line-height: 1.05; }
  .services__label { position: absolute; font-size: 13px; color: var(--ink); text-align: center; width: 90px; line-height: 1.1; }

  .intro {
    position: absolute; left: 62px; top: 628px; width: 738px;
    font-size: 18.5px; line-height: 1.33; text-align: justify; color: var(--ink-soft);
  }
  .intro__initial { float: left; font-size: 74px; line-height: .9; margin: 0 6px 0 0; color: var(--ink); }

  .section-tab {
    position: absolute; left: 0; height: 42px; padding: 0 22px 0 48px;
    background: var(--brand-blue); color: #fff;
    font-size: 27px; line-height: 44px; text-transform: uppercase;
    box-shadow: 0 10px 10px -6px rgba(0,0,0,.35);
  }
  .section-tab--why { top: 750px; width: 252px; }
  .section-tab--lenders { top: 903px; width: 438px; }

  .bullets { position: absolute; list-style: none; font-size: 15px; line-height: 19px; color: var(--ink-soft); }
  .bullets li::before { content: "•"; color: var(--brand-orange); margin-right: 7px; }
  .bullets--why-left { left: 70px; top: 826px; }
  .bullets--why-right { left: 392px; top: 826px; }
  .bullets--lenders-left { left: 70px; top: 1021px; }
  .bullets--lenders-right { left: 278px; top: 1021px; }
  .divider { position: absolute; width: 1px; background: var(--ink); }
  .divider--why { left: 375px; top: 826px; height: 40px; }
  .divider--lenders { left: 263px; top: 1021px; height: 78px; }

  .lenders-intro { position: absolute; left: 50px; top: 968px; width: 560px; font-size: 15px; line-height: 19px; color: var(--ink-soft); }

  .idea-art {
    position: absolute; left: 630px; top: 930px; width: 165px; height: 187px;
    background: linear-gradient(135deg, #f7c623 0%, #f7a21d 45%, #1f5c8c 55%, #123f66 100%);
    border-radius: 80px 80px 0 0;
  }

  .footer {
    position: absolute; left: 0; top: 1117px; width: 832px; height: 55px;
    background: var(--brand-orange); color: #fff;
    display: flex; align-items: center; justify-content: center; gap: 20px; font-size: 15px;
  }
  .footer__sep { width: 1px; height: 24px; background: #fff; }
</style>
</head>
<body>
  <main class="flyer">
    <header>
      <div class="brand">
        <span class="brand__mark"></span>
        <div class="brand__name">Harbourline Capital<br>Partners Pty Ltd</div>
      </div>
      <div class="contact-top">
        <div class="contact-top__web">www.harbourcp-example.com.au</div>
        <div class="contact-top__phone">+61 400 123 987</div>
      </div>
    </header>

    <section class="hero">
      <div class="hero__glow"></div>
      <div class="hero__portrait" role="img" aria-label="Photo of a smiling businesswoman in a brown shirt with arms folded"></div>

      <svg class="services" viewBox="0 0 832 448" aria-hidden="false">
        <circle cx="542" cy="218" r="162" fill="var(--orange-pale)"/>
        <circle cx="542" cy="218" r="150" fill="var(--orange-soft)"/>
        <circle cx="542" cy="218" r="134" fill="var(--brand-orange)"/>
        <g role="img" aria-label="Illustrated vehicle icons for boats, trucks, caravans, earth moving equipment, jet skis and cars">
          <circle cx="549" cy="56" r="46" fill="var(--badge-yellow)"/>
          <circle cx="699" cy="142" r="46" fill="var(--badge-green)"/>
          <circle cx="686" cy="298" r="46" fill="var(--badge-yellow)"/>
          <circle cx="549" cy="385" r="46" fill="var(--badge-salmon)"/>
          <circle cx="410" cy="295" r="46" fill="var(--badge-yellow)"/>
          <circle cx="391" cy="144" r="46" fill="var(--badge-yellow)"/>
        </g>
      </svg>

      <div class="services__title">
        <div class="services__lead">We specialise in</div>
        <div class="services__main">FINANCING</div>
      </div>
      <span class="services__label" style="left:504px;top:80px">Boats</span>
      <span class="services__label" style="left:654px;top:166px">Trucks</span>
      <span class="services__label" style="left:641px;top:320px">Caravans</span>
      <span class="services__label" style="left:504px;top:400px">Earth moving Equipment</span>
      <span class="services__label" style="left:365px;top:318px">Jet skis</span>
      <span class="services__label" style="left:346px;top:168px">Cars</span>
      <div class="hero__rule"></div>
    </section>

    <p class="intro"><span class="intro__initial">H</span>arbourline capital partners is a bespoke brokerage firm established by a team of professionals who bring with them over 50 year's combined experience in consulting, finance, negotiation, and executive roles within the finance and automotive industry. We strive for excellence, delivering the right solution for our clients in a timely and professional manner.</p>

    <h2 class="section-tab section-tab--why">Why use us</h2>
    <ul class="bullets bullets--why-left">
      <li>Low rates</li>
      <li>Access Australia's most trusted lenders</li>
      <li>Quick &amp; easy, same day approvals</li>
    </ul>
    <span class="divider divider--why"></span>
    <ul class="bullets bullets--why-right">
      <li>Professional advice</li>
      <li>New, Used, private or dealer sale - the choice is yours</li>
      <li>100% Finance available</li>
    </ul>

    <h2 class="section-tab section-tab--lenders">Our financiers include</h2>
    <p class="lenders-intro">We have privileged and specialized access to a wide range of lenders enabling us to tailor solutions which cater to your individual needs. We work with:</p>
    <ul class="bullets bullets--lenders-left">
      <li>Southgate Finance</li>
      <li>Meridian Leasing</li>
      <li>Valdor Motor Finance</li>
      <li>Libra Finance</li>
      <li>Peppercorn Asset finance</li>
    </ul>
    <span class="divider divider--lenders"></span>
    <ul class="bullets bullets--lenders-right">
      <li>Norland Finance</li>
      <li>Grove and General Finance</li>
      <li>Kestrel Finance</li>
      <li>Bayview Finance</li>
    </ul>

    <div class="idea-art" role="img" aria-label="Illustration of a head in profile with a light bulb bearing a dollar sign"></div>

    <footer class="footer">
      <span>18 Marlow Street, Fyshwick ACT 2609</span>
      <span class="footer__sep"></span>
      <span>admin@harbourcp-example.com.au</span>
    </footer>
  </main>
</body>
</html>
```